Website for new child psychology practice

New clinical psychology practice in NSW Australia, specialising in work with children, adolescents and families. I would like to feature the colours in the logo, which was recently designed by pixelhive designer Odette.
I am seeking a professional looking page, which is easy to navigate and is colourful and playful but not childish.
Target Market(s)
Parents and professionals
Industry/Entity Type
Health
Coding
Coded - Design and coding required
Number of Pages Required
1 page
Font styles to use
Serif
Requirements
Must have
- Pages for 'About us' 'Services' 'Fees and information' 'Contact us'
Should not have
- Childish stock photos

```html
<!DOCTYPE html>
<html lang="en">
<head>
<meta charset="utf-8">
<title>Dr Nora Ellis – Clinical Psychologist</title>
<link href="https://fonts.googleapis.com/css2?family=Cinzel:wght@400;600&family=Open+Sans:wght@400;600&display=swap" rel="stylesheet">
<style>
:root{
  --purple:#93278f;
  --orange:#f07a3a;
  --grad:linear-gradient(90deg,#f07a3a,#a3288e);
  --ink:#222;
  --body:#444;
  --soft:#f1f1f1;
  --footer:#1f1f1f;
  --white:#fff;
}
*{box-sizing:border-box;margin:0;padding:0}
html,body{width:1200px;height:3549px;overflow:hidden}
body{position:relative;font-family:"Open Sans",sans-serif;color:var(--body);background:var(--white)}
.abs{position:absolute}
.btn{position:absolute;display:flex;align-items:center;justify-content:center;border-radius:24px;font-size:15px;font-weight:600;text-decoration:none}
.btn-grad{background:var(--grad);color:var(--white)}
.btn-white{background:var(--white);color:var(--purple)}
.brand{display:flex;align-items:center;gap:10px;font-family:"Cinzel",serif;font-weight:600;font-size:26px;color:var(--white);letter-spacing:1px}
.brand-dot{width:30px;height:30px;border-radius:50%;background:var(--orange)}

/* hero */
.hero{left:0;top:0;width:1200px;height:537px;
  background:
    linear-gradient(90deg,rgba(147,39,143,0) 0%,rgba(147,39,143,.25) 40%,rgba(142,38,140,.9) 60%,#8e2a8b 100%),
    linear-gradient(180deg,#b9876a 0%,#d8b49a 30%,#c79a84 60%,#e0723f 85%,#c85a34 100%);}
.hero-logo{left:112px;top:38px}
.nav{left:473px;top:44px;display:flex;gap:28px;font-size:15px;color:var(--white)}
.hero-title{right:111px;top:188px;text-align:right;font-family:"Cinzel",serif;font-weight:600;font-size:56px;line-height:62px;color:var(--white)}
.hero-text{right:111px;top:335px;width:420px;text-align:right;font-size:15.5px;line-height:28px;color:var(--white)}
.arrow{position:absolute;width:30px;height:30px}

/* about */
.about{left:0;top:537px;width:1200px;height:630px;background:var(--soft)}
.heading{display:flex;align-items:center;gap:14px;font-family:"Cinzel",serif;font-size:46px;color:var(--ink)}
.heading-dot{width:40px;height:40px;border-radius:50%;background:var(--grad)}
.about-head{left:112px;top:105px}
.about-text{left:112px;top:196px;width:445px;font-size:15.5px;line-height:28.5px}
.about-text p+p{margin-top:17px}
.about-photo{left:667px;top:90px;width:424px;height:424px;border-radius:50%;padding:3px;background:linear-gradient(135deg,#f07a3a,#a3288e)}
.about-photo div{width:100%;height:100%;border-radius:50%;
  background:linear-gradient(180deg,#eceae6 0%,#e2ddd2 28%,#e8d68a 42%,#ddc56e 55%,#4a4c55 70%,#3a3c44 85%,#c97a55 100%)}

/* services */
.services-head{left:0;width:1200px;top:1248px;justify-content:center}
.card{position:absolute;top:1389px;width:283px;height:458px;background:var(--white);box-shadow:0 3px 10px rgba(0,0,0,.1)}
.card-photo{position:absolute;left:10px;top:0;width:263px;height:263px;border-radius:50%;border:4px solid var(--purple)}
.card-photo.orange{border-color:var(--orange)}
.card-icon{position:absolute;left:98px;top:208px;width:86px;height:86px;border-radius:50%;background:var(--purple);border:3px solid #fff;display:flex;align-items:center;justify-content:center}
.card-icon.orange{background:var(--orange)}
.card h3{position:absolute;top:318px;width:100%;text-align:center;font-size:17px;font-weight:600;color:var(--ink)}
.card p{position:absolute;top:352px;left:20px;right:20px;text-align:center;font-size:14px;line-height:27px}

/* call to action */
.cta{left:0;top:2024px;width:1200px;height:440px;
  background:linear-gradient(90deg,#c9a27a 0%,#e4dccd 14%,#b99a78 28%,#e9e4dc 40%,#d2d0cc 55%,#c9c9c9 100%)}
.cta-box{left:533px;top:2089px;width:556px;height:310px;background:linear-gradient(90deg,#ee6c4d,#a3288e);text-align:center;color:var(--white)}
.cta-box h2{font-family:"Cinzel",serif;font-weight:400;font-size:26px;line-height:40px;margin-top:42px}
.cta-box p{font-size:15.5px;line-height:28px;margin:16px auto 0;width:470px}

/* features */
.feature-photo{position:absolute;border-left:8px solid var(--purple)}
.feature-card{position:absolute;background:var(--white);box-shadow:0 3px 12px rgba(0,0,0,.12);text-align:center}
.feature-card h3{font-family:"Cinzel",serif;font-weight:400;font-size:19px;color:var(--ink);margin-top:34px}
.feature-card .rule{width:38px;height:2px;background:var(--orange);margin:10px auto 0}
.feature-card p{font-size:14.5px;line-height:26px;margin:14px 26px 0}

/* footer */
.footer{left:0;top:3191px;width:1200px;height:358px;background:var(--footer);color:#ddd;font-size:14px}
.footer-logo{left:112px;top:102px;font-size:23px}
.contact{left:112px;top:166px;width:240px}
.contact li{list-style:none;display:flex;gap:14px;line-height:26px;margin-bottom:7px}
.contact svg{flex:none;margin-top:6px}
.fcol{position:absolute;top:102px}
.fcol h4{font-size:16px;font-weight:600;color:var(--white)}
.fcol .rule{width:36px;height:2px;background:var(--orange);margin:10px 0 14px}
.fcol li{list-style:none;line-height:30px}
.fcol li::before{content:"› ";color:#fff}
.subscribe{position:relative;width:214px;height:48px;border-radius:24px;background:var(--white);color:#777;font-size:13px;padding:15px 20px}
.subscribe span{position:absolute;right:6px;top:6px;width:38px;height:38px;border-radius:50%;background:var(--grad);display:flex;align-items:center;justify-content:center}
.socials{display:flex;gap:6px;margin-top:18px}
.socials span{width:31px;height:31px;border-radius:50%;border:1.5px solid #ddd;display:flex;align-items:center;justify-content:center}
.copyright{left:0;top:320px;width:1200px;text-align:center;font-size:15px}
</style>
</head>
<body>

<header class="abs hero" role="img" aria-label="Photo of a psychologist playing with letter blocks with a young boy, under a purple overlay"></header>
<div class="abs brand hero-logo"><span class="brand-dot"></span>Dr Nora Ellis</div>
<nav class="abs nav"><span>About us</span><span>Services</span><span>Fees and information</span><span>Contact us</span></nav>
<a class="btn btn-white" style="left:923px;top:39px;width:166px;height:44px">Request Quote</a>
<h1 class="abs hero-title">Empowering<br>Young Minds</h1>
<p class="abs hero-text">Lorem ipsum dolosit amet, consectetur adipiscing elit, sed do eiusmod tempor incididunt ut labore et .</p>
<svg class="arrow" style="left:1013px;top:458px" viewBox="0 0 30 30"><circle cx="15" cy="15" r="13" fill="none" stroke="#fff" stroke-opacity=".7" stroke-width="2"/><path d="M17 9l-6 6 6 6" fill="none" stroke="#fff" stroke-opacity=".7" stroke-width="2"/></svg>
<svg class="arrow" style="left:1058px;top:458px" viewBox="0 0 30 30"><circle cx="15" cy="15" r="13" fill="none" stroke="#fff" stroke-width="2"/><path d="M13 9l6 6-6 6" fill="none" stroke="#fff" stroke-width="2"/></svg>

<section class="abs about">
  <h2 class="abs heading about-head"><span class="heading-dot"></span>About Us</h2>
  <div class="abs about-text">
    <p>Lorem ipsum dolor sit amet, consectetur adipiscing elit, sed do eiusmod tempor incididunt ut labore et dolore magna. Quis ipsum suspene utrices gravidsus commodo viverra.</p>
    <p>Sed ut perspiciatis unde omis iste natus error sit voluptatem acantium doloremque laudantium, tota rem aperiam, eaque ipsa quae ab illo inventore veritatist quasi architecto beatae vitae dicta sunt explicabo. Nemo enim ipsam vluptatem quia voluptas sit aspernatur aut odit at fugit.</p>
  </div>
  <a class="btn btn-grad" style="left:112px;top:481px;width:166px;height:43px">Learn More</a>
  <div class="abs about-photo"><div role="img" aria-label="Photo of a teenage girl in a yellow jumper talking during a session"></div></div>
</section>

<h2 class="abs heading services-head"><span class="heading-dot"></span>Our Services</h2>
<svg class="arrow" style="left:30px;top:1605px" viewBox="0 0 30 30"><circle cx="15" cy="15" r="13" fill="none" stroke="#999" stroke-width="2"/><path d="M17 9l-6 6 6 6" fill="none" stroke="#999" stroke-width="2"/></svg>
<svg class="arrow" style="left:1130px;top:1605px" viewBox="0 0 30 30"><circle cx="15" cy="15" r="13" fill="none" stroke="#555" stroke-width="2"/><path d="M13 9l6 6-6 6" fill="none" stroke="#555" stroke-width="2"/></svg>

<article class="card" style="left:112px">
  <div class="card-photo" role="img" aria-label="Photo of a young woman holding her neck in pain in a park" style="background:linear-gradient(180deg,#a9c47e 0%,#8fb36a 25%,#2e2a2a 42%,#d9cfc4 55%,#86a9cf 72%,#5d86b5 100%)"></div>
  <div class="card-icon"><svg width="40" height="40" viewBox="0 0 40 40" fill="none" stroke="#fff" stroke-width="2"><circle cx="20" cy="13" r="6"/><path d="M8 34v-6a12 12 0 0124 0v6z"/></svg></div>
  <h3>Managing Chronic Pain</h3>
  <p>Lorem ipsum dolor sit amet, con secteturing elit, sed do eiusmod tempor incididunt ut labore.</p>
</article>
<article class="card" style="left:459px">
  <div class="card-photo orange" role="img" aria-label="Photo of a young man looking thoughtful in a session" style="background:linear-gradient(180deg,#c9c6c0 0%,#a89a88 25%,#2f2620 40%,#c08d70 55%,#6e6a3e 72%,#4f4c2c 100%)"></div>
  <div class="card-icon orange"><svg width="40" height="40" viewBox="0 0 40 40" fill="none" stroke="#fff" stroke-width="2"><path d="M12 34v-7c-4-3-5-7-4-11a12 12 0 0123 2l3 6h-3v5h-5v5"/><circle cx="20" cy="16" r="5"/></svg></div>
  <h3>Depression</h3>
  <p>Lorem ipsum dolor sit amet, con secteturing elit, sed do eiusmod tempor incididunt ut labore.</p>
</article>
<article class="card" style="left:806px">
  <div class="card-photo" role="img" aria-label="Photo of a worried young woman standing in a busy corridor" style="background:linear-gradient(180deg,#eeeeee 0%,#e2e3e6 30%,#f4f4f4 50%,#a9bcd6 68%,#7f9cc2 85%,#c9ccd2 100%)"></div>
  <div class="card-icon"><svg width="40" height="40" viewBox="0 0 40 40" fill="none" stroke="#fff" stroke-width="2"><path d="M12 34v-7c-4-3-5-7-4-11a12 12 0 0123 2l3 6h-3v5h-5v5"/><path d="M20 10l-3 7h5l-3 7"/></svg></div>
  <h3>Severe Anxiety Disorders</h3>
  <p>Lorem ipsum dolor sit amet, con secteturing elit, sed do eiusmod tempor incididunt ut labore.</p>
</article>

<section class="abs cta" role="img" aria-label="Photo of a therapist talking with a young girl holding a teddy bear in a bright playroom"></section>
<div class="abs cta-box">
  <h2>Take the first step towards<br>healing and self-discovery</h2>
  <p>Scheduling a session with our compassionate and experienced clinical psychologists today.</p>
  <a class="btn btn-white" style="left:195px;top:221px;width:166px;height:44px">Request Quote</a>
</div>

<div class="feature-photo" role="img" aria-label="Photo of a family drawing together at a table" style="left:112px;top:2553px;width:453px;height:320px;background:linear-gradient(180deg,#eceae4 0%,#d8d6cf 25%,#8f8f8c 45%,#b58e6e 65%,#9a7554 80%,#d9d2c0 100%)"></div>
<div class="feature-card" style="left:163px;top:2789px;width:358px;height:276px">
  <h3>Fees and information</h3><div class="rule"></div>
  <p>Lorem ipsum dolor sit amet, consectetur adipiscing elit, sed do eiusmopor incididunt ut lore et dolore magna aliqua. Quis ipsum suspendisse ultrices gravida.</p>
  <a class="btn btn-grad" style="left:96px;top:194px;width:166px;height:43px">Learn More</a>
</div>

<div class="feature-photo" role="img" aria-label="Portrait photo of a smiling psychologist with glasses" style="left:634px;top:2614px;width:455px;height:318px;border-left-color:var(--orange);background:linear-gradient(90deg,#5a4a40 0%,#7a6656 25%,#5b3a28 40%,#c99478 52%,#5b3a28 66%,#8a8270 85%,#4a4a40 100%)"></div>
<div class="feature-card" style="left:685px;top:2848px;width:360px;height:276px">
  <h3>Dr. Nora Ellis</h3><div class="rule"></div>
  <p>Lorem ipsum dolor sit amet, consectetur adipiscing elit, sed do eiusmopor incididunt ut lore et dolore magna aliqua. Quis ipsum suspendisse ultrices gravida.</p>
  <a class="btn btn-grad" style="left:97px;top:194px;width:166px;height:43px">Learn More</a>
</div>

<footer class="abs footer">
  <div class="abs brand footer-logo"><span class="brand-dot" style="width:24px;height:24px"></span>Dr Nora Ellis</div>
  <ul class="abs contact">
    <li><svg width="14" height="16" viewBox="0 0 14 16"><path d="M7 0a6 6 0 00-6 6c0 4 6 10 6 10s6-6 6-10a6 6 0 00-6-6zm0 8a2 2 0 110-4 2 2 0 010 4z" fill="#f07a3a"/></svg><span>Dr.Nora Ellis,<br>Address Comes Here</span></li>
    <li><svg width="14" height="14" viewBox="0 0 14 14"><path d="M3 0l3 3-2 2a8 8 0 005 5l2-2 3 3-2 3C6 14 0 8 0 3z" fill="#f07a3a"/></svg><span>+1 555-010-2030</span></li>
    <li><svg width="14" height="12" viewBox="0 0 14 12"><rect width="14" height="12" rx="1" fill="#f07a3a"/><path d="M1 2l6 4 6-4" fill="none" stroke="#1f1f1f" stroke-width="1.3"/></svg><span>info@drnoraellis.com</span></li>
  </ul>
  <div class="fcol" style="left:441px"><h4>QUICK LINKS</h4><div class="rule"></div>
    <ul><li>About Us</li><li>Services</li><li>Fees and information</li><li>Contact Us</li></ul></div>
  <div class="fcol" style="left:656px"><h4>SERVICES</h4><div class="rule"></div>
    <ul><li>Terms &amp; Conditions</li><li>Privacy Statement</li><li>Help Centre</li></ul></div>
  <div class="fcol" style="left:870px"><h4>SUBSCRIBE TO US</h4><div class="rule"></div>
    <div class="subscribe">Email ID<span><svg width="16" height="16" viewBox="0 0 16 16"><path d="M2 2l13 6-13 6 3-6z" fill="#fff"/></svg></span></div>
    <div class="socials" aria-label="Social media links">
      <span><svg width="14" height="14" viewBox="0 0 14 14" fill="none" stroke="#ddd" stroke-width="1.4"><circle cx="7" cy="7" r="5.5"/><path d="M1.5 7h11M7 1.5c2 2 2 9 0 11M7 1.5c-2 2-2 9 0 11"/></svg></span>
      <span><svg width="14" height="14" viewBox="0 0 14 14" fill="none" stroke="#ddd" stroke-width="1.4"><path d="M6 8l2-2M5 6.5L3.5 8a2 2 0 003 3L8 9.5M9 7.5L10.5 6a2 2 0 00-3-3L6 4.5"/></svg></span>
      <span><svg width="14" height="14" viewBox="0 0 14 14" fill="none" stroke="#ddd" stroke-width="1.4"><path d="M2 3h10v7H6l-3 2v-2H2z"/></svg></span>
      <span><svg width="14" height="14" viewBox="0 0 14 14" fill="none" stroke="#ddd" stroke-width="1.4"><circle cx="10" cy="3.5" r="1.5"/><circle cx="4" cy="7" r="1.5"/><circle cx="10" cy="10.5" r="1.5"/><path d="M5.3 6.2l3.4-2M5.3 7.8l3.4 2"/></svg></span>
    </div>
  </div>
  <p class="abs copyright">2024 Dr.Nora Ellis. All Rights Reserved.</p>
</footer>

</body>
</html>
```